Popup Banners - BrightCounsel - Legal Technology

- We need two banners (same style) designed with two different images and different text.

- The details of the printing requirements are attached, along with suggested images.

- The banners should share the same theme as our website www.brightcounsel.com.au

- The first banner would include our logo (attached), use the 'roads join' image (attached) in some way and text: New Opportunities - Where legal services and technology meet.

- The second banner would include our logo (attached), use the 'jigsaw' image (attached) in some way and use text: Legal Technology Strategy, Advice and Capability.

- Details on what are required from the Printer is attached also.

Target Market(s)

Legal Professionals

Industry/Entity Type

Information Technology

Font styles to use
Sans Serif

Requirements
Must have
• Our logo (attached), suggested text and the image mentioned for each.
Nice to have
• Professional and modern look
Should not have
• Cheap looking

```html
<!DOCTYPE html>
<html lang="en">
<head>
<meta charset="utf-8">
<title>BrightCounsel – Legal Technology Banner</title>
<link rel="stylesheet" href="https://fonts.googleapis.com/css2?family=Dosis:wght@500&family=Montserrat:wght@500&display=swap">
<style>
  :root {
    --paper: #ffffff;
    --brand-ink: #4a4440;
    --brand-blue: #4f9fd8;
    --deep-navy: #0e1f2f;
    --mid-blue: #2a5270;
    --soft-blue: #8cc3e6;
    --glow: #f2faff;
    --headline: #ffffff;
  }
  html, body {
    margin: 0;
    padding: 0;
    overflow: hidden;
    background: var(--paper);
  }
  .banner {
    position: relative;
    width: 1200px;
    height: 2906px;
    background: var(--paper);
    overflow: hidden;
  }
  .brand {
    position: absolute;
    top: 220px;
    left: 0;
    width: 1200px;
    display: flex;
    align-items: center;
    justify-content: center;
    gap: 40px;
  }
  .brand-square {
    width: 80px;
    height: 80px;
    background: var(--brand-blue);
  }
  .brand-name {
    font-family: "Montserrat", sans-serif;
    font-weight: 500;
    font-size: 80px;
    letter-spacing: 18px;
    color: var(--brand-ink);
    line-height: 1;
  }
  .hero {
    position: absolute;
    left: 0;
    top: 0;
    width: 1200px;
    height: 2906px;
  }
  .headline {
    position: absolute;
    top: 648px;
    left: 0;
    width: 1172px;
    margin: 0;
    text-align: center;
    font-family: "Dosis", sans-serif;
    font-weight: 500;
    font-size: 110px;
    line-height: 144px;
    color: var(--headline);
  }
  .headline span { display: block; }
</style>
</head>
<body>
<main class="banner">
  <header class="brand">
    <div class="brand-square"></div>
    <div class="brand-name">BrightCounsel</div>
  </header>

  <svg class="hero" viewBox="0 0 1200 2906">
    <defs>
      <radialGradient id="heroGlow" cx="0.56" cy="0.42" r="0.62">
        <stop offset="0" stop-color="var(--glow)"/>
        <stop offset="0.18" stop-color="var(--soft-blue)"/>
        <stop offset="0.5" stop-color="var(--mid-blue)"/>
        <stop offset="1" stop-color="var(--deep-navy)"/>
      </radialGradient>
      <clipPath id="heroShape">
        <path d="M0 672 C 300 560, 800 475, 1200 468 L 1200 2280 C 1140 2500, 1080 2700, 1032 2906 L 0 2906 Z"/>
      </clipPath>
    </defs>
    <g clip-path="url(#heroShape)">
      <rect x="0" y="440" width="1200" height="2466" fill="url(#heroGlow)" role="img" aria-label="Photo of a hand lifting a glowing jigsaw puzzle piece out of a blue puzzle"/>
      <polygon class="accent-band" points="1200,560 1200,1040 920,1040" fill="#ffffff" fill-opacity="0.12"/>
      <polygon class="accent-band" points="0,1212 264,1212 0,1500" fill="#ffffff" fill-opacity="0.12"/>
    </g>
  </svg>

  <h1 class="headline">
    <span>Legal&nbsp;&nbsp;Technology</span>
    <span>Strategy,</span>
    <span>Advice and Capability</span>
  </h1>
</main>
</body>
</html>
```